Business Card Design For A Renovation Contractor Company

We need a business card for a new company based in Singapore, our company name is "KM Bravant". We are a renovation contractor that builds designs into reality. We build more of F&B restaurants, retail stores and commercial offices. We work very closely with designers. The final design should communicate to our client that we are a company that you can trust, that will plan and complete your project without giving you a headache. I like my client to remember my company as "KM". The beauty of SIMPLE is important.

Industry/Entity Type

Contractor

Requirements
Nice to have
• Black or Red base

```html
<!DOCTYPE html>
<html lang="en">
<head>
<meta charset="utf-8">
<title>KM Bravant — Business Card</title>
<link rel="stylesheet" href="https://fonts.googleapis.com/css2?family=Didact+Gothic&family=Open+Sans:wght@700&display=swap">
<style>
  :root {
    --page: #e9e6e1;
    --card-dark: #141414;
    --card-mid: #2b2c2e;
    --red: #e0141e;
    --red-deep: #9e0b12;
    --white: #ffffff;
    --grey: #b9b9b9;
  }
  * { margin: 0; padding: 0; box-sizing: border-box; }
  html, body { width: 911px; height: 1200px; overflow: hidden; }
  body {
    background: var(--page);
    font-family: "Didact Gothic", "Helvetica Neue", Arial, sans-serif;
    color: var(--white);
    position: relative;
  }
  .card {
    position: absolute;
    left: 135px;
    width: 640px;
    height: 366px;
    border-radius: 4px;
    overflow: hidden;
    background: linear-gradient(135deg, var(--card-mid) 0%, var(--card-dark) 60%, #0b0b0b 100%);
    box-shadow: 0 10px 30px rgba(0,0,0,.25);
  }
  .card--front { top: 180px; }
  .card--back { top: 654px; }

  .card__sweep { position: absolute; left: 0; top: 0; width: 120px; height: 366px; }

  .brand { position: absolute; left: 130px; top: 46px; display: flex; align-items: center; gap: 16px; }
  .brand__dot { width: 54px; height: 54px; border-radius: 50%; background: var(--red); flex: none; }
  .brand__text { display: flex; flex-direction: column; }
  .brand__name { font-size: 38px; line-height: 1; letter-spacing: .5px; color: var(--white); }
  .brand__tagline { font-size: 14px; color: var(--grey); margin-top: 6px; border-top: 1px solid var(--grey); padding-top: 3px; }

  .person { position: absolute; left: 350px; top: 150px; }
  .person__name { font-family: "Open Sans", Arial, sans-serif; font-weight: 700; font-size: 22px; letter-spacing: 1px; }
  .person__name .last { color: var(--red); }
  .person__role { font-size: 12px; color: var(--grey); margin-top: 2px; }

  .contact { position: absolute; left: 130px; top: 206px; font-size: 12.5px; color: var(--grey); line-height: 1.5; }
  .contact__address { margin-bottom: 8px; width: 300px; }
  .contact__row { display: flex; align-items: center; gap: 10px; }
  .contact__row svg { width: 12px; height: 12px; fill: var(--red); flex: none; }

  .back-brand { position: absolute; left: 130px; top: 130px; display: flex; align-items: center; gap: 22px; }
  .back-brand__dot { width: 90px; height: 90px; border-radius: 50%; background: var(--red); flex: none; }
  .back-brand__name { font-size: 52px; line-height: 1; color: var(--white); }
  .back-brand__tagline { font-size: 16px; color: var(--grey); margin-top: 8px; }
  .back-url { position: absolute; right: 34px; bottom: 26px; font-size: 12px; color: var(--grey); }
</style>
</head>
<body>

  <section class="card card--front">
    <svg class="card__sweep" viewBox="0 0 120 366" preserveAspectRatio="none" aria-hidden="true">
      <path d="M0 0 H18 C70 110 70 250 30 366 H0 Z" fill="var(--red)"/>
      <path d="M18 0 C70 110 70 250 30 366 H38 C80 250 80 110 26 0 Z" fill="var(--white)"/>
    </svg>

    <div class="brand">
      <span class="brand__dot"></span>
      <div class="brand__text">
        <span class="brand__name">KM Bravant</span>
        <span class="brand__tagline">from plan to finished space</span>
      </div>
    </div>

    <div class="person">
      <div class="person__name">FirstN <span class="last">LastN</span></div>
      <div class="person__role">Owner</div>
    </div>

    <div class="contact">
      <p class="contact__address">Tanjong Lane #03-120 Harbour Point Singapore 408812</p>
      <div class="contact__row">
        <svg viewBox="0 0 24 24" aria-hidden="true"><path d="M6.6 10.8a15 15 0 006.6 6.6l2.2-2.2c.3-.3.7-.4 1-.2 1.1.4 2.3.6 3.6.6.6 0 1 .4 1 1V20c0 .6-.4 1-1 1A17 17 0 013 4c0-.6.4-1 1-1h3.5c.6 0 1 .4 1 1 0 1.3.2 2.5.6 3.6.1.3 0 .7-.2 1z"/></svg>
        <span>000-000-0000</span>
      </div>
      <div class="contact__row">
        <svg viewBox="0 0 24 24" aria-hidden="true"><path d="M6 3h12v5H6zM3 9h18v8h-3v4H6v-4H3zm5 6v4h8v-4z"/></svg>
        <span>000-000-0001</span>
      </div>
      <div class="contact__row">
        <svg viewBox="0 0 24 24" aria-hidden="true"><path d="M7 1h10a2 2 0 012 2v18a2 2 0 01-2 2H7a2 2 0 01-2-2V3a2 2 0 012-2zm0 3v14h10V4z"/></svg>
        <span>000-000-0000</span>
      </div>
      <div class="contact__row">
        <svg viewBox="0 0 24 24" aria-hidden="true"><path d="M2 5h20v14H2zm2 2v.5l8 5 8-5V7z"/></svg>
        <span>mail@kmbravant.com</span>
      </div>
      <div class="contact__row">
        <svg viewBox="0 0 24 24" aria-hidden="true"><path d="M12 2a10 10 0 100 20 10 10 0 000-20zm0 2c1 1.2 1.8 3.3 2 6h-4c.2-2.7 1-4.8 2-6zM4.1 11h3.9c.1 2.5.7 4.6 1.6 6.2A8 8 0 014.1 11zm11.9 0h3.9a8 8 0 01-5.5 6.2c.9-1.6 1.5-3.7 1.6-6.2zm-6 0h4c-.2 2.7-1 4.8-2 6-1-1.2-1.8-3.3-2-6z"/></svg>
        <span>www.kmbravant.com</span>
      </div>
    </div>
  </section>

  <section class="card card--back">
    <svg class="card__sweep" viewBox="0 0 120 366" preserveAspectRatio="none" aria-hidden="true">
      <path d="M0 0 H10 C40 120 40 250 16 366 H0 Z" fill="var(--red)"/>
    </svg>
    <div class="back-brand">
      <span class="back-brand__dot"></span>
      <div>
        <div class="back-brand__name">KM Bravant</div>
        <div class="back-brand__tagline">from plan to finished space</div>
      </div>
    </div>
    <div class="back-url">www.kmbravant.com</div>
  </section>

</body>
</html>
```